Social Media Marketing website

Need website designed for social media marketing company PlumeVista.com
Do no currently have logo.
Pages:
Main
Services
Order
Contact
Please use dummy text for now. I will provide content to winner later to add.
Main page should clearly show the steps with some sort of graphic: Establish, Engage, Analyze.
Services provided (steps):
1) Establish social media presence
2) Social media management and advertising
3) Analyze and engage
Site should be simple, clean and attractive. Design examples:
http://brindlow.com/
http://www.quillmarkhub.com/
http://www.fenwaterlyx.com/
Be creative! It should not look like a template.
Updates
Updated examples.
Contact me for questions.
owen@plumevista.com
3) Analyze and engage
Advertising

```html
<!DOCTYPE html>
<html lang="en">
<head>
<meta charset="utf-8">
<title>PlumeVista — Social Media Marketing</title>
<link rel="stylesheet" href="https://fonts.googleapis.com/css2?family=Open+Sans:wght@400;600;700&family=Ubuntu:wght@400;500&display=swap">
<style>
:root{
  --blue:#1a9be6;
  --blue-light:#22b4ff;
  --blue-deep:#0a86d8;
  --title-blue:#1b8bd8;
  --link-blue:#1466c0;
  --ink:#222;
  --text:#333;
  --muted:#666;
  --header-bg:#e9e9e9;
  --steps-bg:#e3e3e3;
  --rule:#c9c9c9;
  --bar-dark:#1e1e1e;
  --footer-bg:#7f7f7f;
  --tag-bg:#e2e2e2;
  --white:#fff;
}
*{box-sizing:border-box;margin:0;padding:0}
html,body{width:836px;height:1200px;overflow:hidden;background:var(--white)}
body{position:relative;font-family:"Open Sans",Arial,sans-serif;color:var(--text);font-size:8.5px;line-height:1.6}
a{color:var(--link-blue)}
.abs{position:absolute}

/* header */
.site-header{position:absolute;left:0;top:0;width:836px;height:91px;background:var(--header-bg)}
.brand{position:absolute;left:116px;top:22px;font:700 26px/1 "Open Sans",sans-serif;color:#3a3a3a;letter-spacing:-.5px}
.main-nav{position:absolute;left:439px;top:36px;display:flex;align-items:center;font-size:9.5px;color:var(--ink)}
.main-nav a{color:var(--ink);text-decoration:none;margin-right:28px}
.main-nav .is-active{background:var(--blue);color:var(--white);border:2px solid var(--white);box-shadow:0 0 0 1px #b8d8ee;padding:3px 13px;margin-right:30px}

/* hero */
.hero{position:absolute;left:0;top:91px;width:836px;height:276px;background:linear-gradient(90deg,var(--blue-deep),var(--blue-light))}
.hero-title{position:absolute;left:71px;top:32px;font:700 30px/1 "Open Sans",sans-serif;color:var(--white)}
.hero-sub{position:absolute;left:71px;top:74px;font:700 15px/1 "Open Sans",sans-serif;color:#0a0a0a}
.hero-text{position:absolute;left:71px;top:108px;width:330px;color:var(--white);font-size:10px;line-height:1.55}
.hero-points{position:absolute;left:71px;top:154px;width:326px;height:44px;border:1px solid rgba(255,255,255,.55);background:rgba(255,255,255,.06);display:grid;grid-template-columns:1fr 1fr;padding:5px 10px;color:var(--white);font-size:8px;list-style:none}
.hero-points li::before{content:"";display:inline-block;width:4px;height:4px;background:#bfe6ff;margin-right:9px;vertical-align:middle}
.btn-hero{position:absolute;top:220px;height:22px;border:1px solid #9fd6ff;background:linear-gradient(#3bb0f2,#168fdc);color:var(--white);font:700 12px/20px "Open Sans",sans-serif;text-align:center}
.hero-photo{position:absolute;left:509px;top:4px;width:289px;height:270px;border:3px solid var(--white);background:linear-gradient(160deg,#e6e3c6 0%,#c7b37a 45%,#8a6a3e 75%,#6a4c34 100%)}

/* social bar */
.social-bar{position:absolute;left:0;top:367px;width:836px;height:40px;background:linear-gradient(#3a3a3a,var(--bar-dark))}
.social-link{position:absolute;top:14px;color:#dcdcdc;font-size:8px;display:flex;align-items:center}
.social-link i{display:inline-block;width:10px;height:10px;background:#7bb8de;margin-right:9px}
.social-link.rss i{background:#f0a030}

/* steps */
.steps{position:absolute;left:0;top:407px;width:836px;height:200px;background:var(--steps-bg)}
.step{position:absolute;top:0;width:230px;height:200px}
.step h2{position:absolute;left:0;top:34px;font:400 19px/1 "Ubuntu",sans-serif;color:var(--title-blue)}
.step svg{position:absolute;left:-4px;top:72px}
.step p{position:absolute;left:56px;top:76px;width:160px;font-size:8px;line-height:1.6;color:var(--ink)}
.step .btn-more{position:absolute;left:56px;top:156px;width:98px;height:18px;border:1px solid #bdbdbd;background:#f1f1f1;font-size:7.5px;line-height:16px;text-align:center;color:#555}
.step-divider{position:absolute;top:22px;width:1px;height:160px;background:#cfcfcf}

/* content */
.section-title{position:absolute;font:400 18px/1 "Ubuntu",sans-serif;color:var(--title-blue)}
.news-date{position:absolute;left:72px;font-size:9px;color:var(--link-blue)}
.news-date span{color:#555;margin:0 8px}
.body-copy{position:absolute;font-size:8px;line-height:2;color:var(--ink)}
.read-more{position:absolute;left:72px;font-size:7.5px;color:var(--link-blue);text-decoration:underline}
.form-label{position:absolute;left:76px;font-size:8px;color:var(--ink)}
.form-input{position:absolute;left:76px;width:137px;height:15px;border:1px solid #bbb;background:var(--white)}
.btn-subscribe{position:absolute;left:223px;top:1016px;width:54px;height:18px;border:1px solid #c6c6c6;background:#ececec;font-size:7.5px;line-height:16px;text-align:center}
.rule{position:absolute;left:329px;width:458px;height:2px;background:var(--rule)}
.link-list{position:absolute;left:333px;top:775px;width:440px;display:grid;grid-template-columns:1fr 1fr;row-gap:6px;list-style:none;font-size:7.5px}
.link-list li::before{content:"";display:inline-block;width:5px;height:5px;background:#c8d4de;margin-right:8px;vertical-align:middle}
.link-list a{text-decoration:underline}
.tag{position:absolute;left:332px;height:17px;padding:0 7px;background:var(--tag-bg);font-size:7.5px;line-height:17px;color:var(--ink)}

/* footer */
.site-footer{position:absolute;left:0;top:1140px;width:836px;height:60px;background:linear-gradient(#8a8a8a,#767676)}
.footer-nav{position:absolute;left:85px;top:22px;display:flex;gap:18px;font-size:7.5px}
.footer-nav a{color:var(--white);text-decoration:underline}
.copyright{position:absolute;left:553px;top:24px;font-size:7px;color:#eee}
</style>
</head>
<body>

<header class="site-header">
  <div class="brand">PlumeVista</div>
  <nav class="main-nav">
    <a class="is-active" href="#">Home</a>
    <a href="#">Services</a>
    <a href="#">Order</a>
    <a href="#">Contact us</a>
  </nav>
</header>

<section class="hero">
  <h1 class="hero-title">Seriously, though</h1>
  <p class="hero-sub">what to DO in this cold weather?</p>
  <p class="hero-text">Lorem Ipsum has been the industry's standard dummy text ever since the 1500s, when an unknown printer.</p>
  <ul class="hero-points">
    <li>Been the industry's standard dum.</li>
    <li>Simply dummy text orem Ipsum.</li>
    <li>Simply dummy text orem Ipsum.</li>
    <li>Been the industry's standard dum.</li>
  </ul>
  <div class="btn-hero" style="left:71px;width:80px">Sign up!</div>
  <div class="btn-hero" style="left:164px;width:80px">Read more</div>
  <div class="hero-photo" role="img" aria-label="Photo of a woman in a patterned robe relaxing on a brown sofa"></div>
</section>

<div class="social-bar">
  <div class="social-link" style="left:71px"><i></i>Follow us on Chirpline</div>
  <div class="social-link rss" style="left:183px"><i></i>Rss Feed</div>
</div>

<section class="steps">
  <div class="step" style="left:79px">
    <h2>Establish</h2>
    <svg width="40" height="40" viewBox="0 0 40 40"><circle cx="20" cy="20" r="17" fill="#5aa2e6" stroke="#b9dbf7" stroke-width="2"/><circle cx="20" cy="12" r="2.6" fill="#fff"/><rect x="17.6" y="17" width="4.8" height="13" rx="1.5" fill="#fff"/></svg>
    <p>Establish social media presence.<br>Vestibulum sit amet neque cu neque suscipit consequat quis vel risus. Vestibulum vehicula purus mc dia accumsan fermentum.</p>
    <div class="btn-more">more information</div>
  </div>
  <div class="step-divider" style="left:297px"></div>
  <div class="step" style="left:321px">
    <h2>Engage</h2>
    <svg width="40" height="40" viewBox="0 0 40 40"><rect x="3" y="6" width="34" height="22" rx="2" fill="#8fa9c4"/><rect x="6" y="9" width="28" height="16" fill="#cfe2f6"/><rect x="17" y="28" width="6" height="5" fill="#9aa8b6"/><rect x="11" y="33" width="18" height="3" rx="1" fill="#b0bcc8"/></svg>
    <p>Social media management and advertising.<br>Sit amet neque cu neque suscipit consequat quis vel risus. Vestibulum vehicula purus mc dia accumsan</p>
    <div class="btn-more">more information</div>
  </div>
  <div class="step-divider" style="left:547px"></div>
  <div class="step" style="left:572px">
    <h2>Analyze</h2>
    <svg width="40" height="40" viewBox="0 0 40 40"><path d="M5 7h30a3 3 0 0 1 3 3v16a3 3 0 0 1-3 3H17l-8 7v-7H5a3 3 0 0 1-3-3V10a3 3 0 0 1 3-3z" fill="#5f9be8"/><circle cx="13" cy="18" r="2" fill="#fff"/><circle cx="20" cy="18" r="2" fill="#fff"/><circle cx="27" cy="18" r="2" fill="#fff"/></svg>
    <p>Analyze and engage.<br>Vestibulum sit amet neque cu neque suscipit consequat quis vel risus. Vestibulum vehicula purus mc dia accumsan fermentum.</p>
    <div class="btn-more">more information</div>
  </div>
</section>

<main>
  <h2 class="section-title" style="left:72px;top:632px">Latest news</h2>
  <div class="news-date" style="top:667px">22.11.09<span>|</span><a href="#">Lorem ipsum dummy ...</a></div>
  <p class="body-copy" style="left:72px;top:697px;width:215px">Has been the industry's standard dummy text ever since then, when an unknown printer. Simply dummy text of the printing industry...</p>
  <a class="read-more" href="#" style="top:752px">read more</a>
  <div class="news-date" style="top:799px">02.09.09<span>|</span><a href="#">Ipsum dummy ...</a></div>
  <p class="body-copy" style="left:72px;top:829px;width:215px">Standard dummy text ever since then, when an unkn printer. Simply dummy text of the printing and typesetting industry...</p>
  <a class="read-more" href="#" style="top:883px">read more</a>

  <h2 class="section-title" style="left:72px;top:934px;font-size:16px">Subsribe to our newsletter</h2>
  <label class="form-label" style="top:966px">Your Name:</label>
  <div class="form-input" style="top:981px"></div>
  <label class="form-label" style="top:1003px">E-mail address:</label>
  <div class="form-input" style="top:1019px"></div>
  <div class="btn-subscribe">subscribe</div>
  <a class="read-more" href="#" style="left:80px;top:1044px;font-size:8px">Forgot Password?</a>

  <h2 class="section-title" style="left:329px;top:634px">Welcome to PlumeVista</h2>
  <p class="body-copy" style="left:331px;top:660px">Simply dummy text of the printing and typesetting industry.</p>
  <p class="body-copy" style="left:331px;top:690px;width:318px">Lorem Ipsum has been the industry's standard dummy text ever since then, when an unknown printer. Simply dummy text of the <a href="#">printing and typesetting industry</a>. Lorem Ipsum has been the industry's standard <a href="#">dummy text</a> ever since.</p>
  <div class="abs" role="img" aria-label="Illustration of a globe with a compass" style="left:702px;top:674px;width:58px;height:58px;border-radius:50%;background:radial-gradient(circle at 35% 35%,#8fd0ff,#2a7fd0 60%,#2f8a3c)"></div>
  <div class="rule" style="top:760px"></div>
  <ul class="link-list">
    <li><a href="#">Been the industry's standard dummy.</a></li>
    <li><a href="#">Simply dummy text orem.</a></li>
    <li><a href="#">Simply dummy text orem.</a></li>
    <li><a href="#">Undustry's standard dummy text.</a></li>
  </ul>
  <div class="rule" style="top:832px"></div>

  <h2 class="section-title" style="left:329px;top:863px">What we offer</h2>
  <div class="abs" role="img" aria-label="Illustration of photo prints with a magnifying glass" style="left:344px;top:893px;width:80px;height:74px;background:linear-gradient(135deg,#d9ecfb,#5aa0d8 60%,#3a4a5a)"></div>
  <p class="body-copy" style="left:444px;top:889px">Simply dummy text of the printing and typesetting industry.</p>
  <p class="body-copy" style="left:444px;top:919px;width:340px">Lorem Ipsum has been the industry's standard dummy text ever since then, when an unknown printer. Simply dummy text of the <a href="#">printing and typesetting industry</a>. Lorem Ipsum has been the industry's standard dummy text ever since.</p>
  <div class="tag" style="top:993px">Been the industry's standard dummy text ever since then, when inter.</div>
  <div class="tag" style="top:1016px">Simply dummy text orem Ipsum has standard dummy text ever since then, when an unknown.</div>
  <div class="tag" style="top:1039px">Undustry's standard dummy text ever since then, when inter.</div>
</main>

<footer class="site-footer">
  <nav class="footer-nav">
    <a href="#">home</a><a href="#">services</a><a href="#">order</a><a href="#">about</a><a href="#">contact</a><a href="#">rss feed</a>
  </nav>
  <p class="copyright">© Copyright 2011 | plumevista.com. All Rights Reserved</p>
</footer>

</body>
</html>
```